Cosmetic injections clinic needs a fresh looking business card

We need a business card using the supplied logo and color scheme to attract future clients to our clinic. It should be modern and fresh, eye catching and not too busy. Simple and to the point is best. I would like two sided designs with the front indicating address and contact information, and the back in full color with white logo and descriptive information also provided.
Target Market(s)
Clients looking for non surgical beauty enhancements.
Contact Information for Business Card
MeloraSkin
14, 618 Birchmont Way
St. Albert, Alberta
K2P 7W3
Phone: 587-412-6630
Email: info@meloraskin.com
Requirements
Must have
- -Logo supplied with the name and address of the clinic
- -Back of card in full color with white logo with A small line of text indicating both of the following: Anti aging consultants and cosmetic injectables
- Located inside the Voyager Wellness Group

```html
<!DOCTYPE html>
<html lang="en">
<head>
<meta charset="utf-8">
<title>MeloraSkin — Business Card</title>
<link href="https://fonts.googleapis.com/css2?family=Montserrat:wght@500;600&family=Dancing+Script:wght@600&display=swap" rel="stylesheet">
<style>
  :root {
    --purple: #6a3fa3;
    --purple-deep: #5a3394;
    --purple-light: #7d52b3;
    --pink: #e8459c;
    --ink: #2e2b45;
    --paper: #ffffff;
    --backdrop: #ece9ef;
  }
  * { margin: 0; padding: 0; box-sizing: border-box; }
  html, body {
    width: 1200px; height: 1200px; overflow: hidden;
    background: var(--backdrop);
    font-family: "Montserrat", sans-serif;
  }
  .sheet {
    width: 1200px; height: 1200px;
    display: flex; flex-direction: column; align-items: center; justify-content: center;
    gap: 60px;
  }
  .card {
    width: 840px; height: 480px;
    border-radius: 6px;
    box-shadow: 0 10px 30px rgba(40, 20, 70, 0.15);
    position: relative;
    overflow: hidden;
  }
  /* Front */
  .card-front {
    background: var(--paper);
    padding: 70px 0 0 150px;
  }
  .card-front .brand {
    display: flex; align-items: center; gap: 14px;
    margin: 0 0 20px 210px;
  }
  .brand-dot {
    width: 30px; height: 30px; border-radius: 50%;
    background: var(--purple);
  }
  .brand-name {
    font-weight: 600; font-size: 46px; color: var(--purple);
    letter-spacing: 1px;
  }
  .tagline {
    font-family: "Dancing Script", cursive;
    font-size: 32px; color: var(--purple);
    margin-bottom: 26px;
  }
  .phone {
    font-weight: 600; font-size: 25px; color: var(--pink);
    letter-spacing: 1px; margin: 0 0 16px 40px;
  }
  .address {
    font-style: normal; font-weight: 500; font-size: 22px; color: var(--ink);
    line-height: 1.35; margin: 0 0 14px 40px;
  }
  .email {
    font-weight: 500; font-size: 20px; color: var(--ink);
    margin-left: 40px;
  }
  /* Back */
  .card-back {
    background: linear-gradient(135deg, var(--purple-deep), var(--purple) 55%, var(--purple-light));
    display: flex; flex-direction: column; align-items: center;
    padding-top: 110px;
    color: var(--paper);
  }
  .card-back .brand { display: flex; align-items: center; gap: 16px; margin-bottom: 28px; }
  .card-back .brand-dot { background: var(--paper); width: 40px; height: 40px; }
  .card-back .brand-name { color: var(--paper); font-size: 62px; }
  .back-tagline {
    font-family: "Dancing Script", cursive;
    font-size: 32px; color: var(--paper);
    margin-bottom: 12px;
  }
  .location {
    font-weight: 500; font-size: 18px; color: var(--paper);
    letter-spacing: 0.5px;
  }
  .card-back .email {
    color: var(--paper); font-size: 20px; margin: 0;
    position: absolute; left: 60px; bottom: 44px;
  }
</style>
</head>
<body>
<main class="sheet">
  <section class="card card-front" aria-label="Card front">
    <div class="brand">
      <span class="brand-dot"></span>
      <span class="brand-name">MeloraSkin</span>
    </div>
    <p class="tagline">Anti aging consultants and cosmetic injectables</p>
    <p class="phone">PHONE: 587-412-6630</p>
    <address class="address">14, 618 Birchmont Way<br>St. Albert, Alberta<br>K2P 7W3</address>
    <p class="email">Email: info@meloraskin.com</p>
  </section>

  <section class="card card-back" aria-label="Card back">
    <div class="brand">
      <span class="brand-dot"></span>
      <span class="brand-name">MeloraSkin</span>
    </div>
    <p class="back-tagline">Anti aging consultants and cosmetic injectables</p>
    <p class="location">Located inside the Voyager Wellness Group</p>
    <p class="email">Email: info@meloraskin.com</p>
  </section>
</main>
</body>
</html>
```